Business Card Design

We need a business card for a well established Semi Trailer Hire company. I am looking for a new start as we are moving so would like to update our Business Cards and Letter heads.
We hire Semi Trailers to Transport companies.
The colour of our Trailers are Cherry Red so this must be the prominent colour.
I do not want any pictures of trailers on the design.
I do not want the design to be flowery in anyway as we are in the transport industry.
Simple yet effective

Trovan Hire Pty Ltd
Ros Dunmore
Director
Ph: 03 9412 5083
Mobile: 0421 736 209
ros.dunmore@trovanhire.com.au
www.trovanhire.com.au
214-220 Pellow Road, Yarraville

```html
<!DOCTYPE html>
<html lang="en">
<head>
<meta charset="utf-8">
<title>Trovan Hire Pty Ltd – Business Card</title>
<link rel="stylesheet" href="https://fonts.googleapis.com/css2?family=Lato:wght@400;700&display=swap">
<style>
  :root {
    --cherry: #e8232a;
    --panel-grey: #dcdcdd;
    --panel-light: #ececed;
    --card-white: #f7f7f7;
    --ink-grey: #5b5b5d;
    --bevel: #a9a9ab;
    --backdrop: #e9e4dc;
  }
  * { margin: 0; padding: 0; box-sizing: border-box; }
  html, body {
    width: 1200px;
    height: 900px;
    overflow: hidden;
    background: var(--backdrop);
  }
  .canvas {
    width: 1200px;
    height: 900px;
    display: flex;
    flex-direction: column;
    align-items: center;
    justify-content: center;
    gap: 56px;
  }
  .card {
    width: 640px;
    height: 366px;
    display: block;
    box-shadow: 0 6px 18px rgba(0,0,0,0.18);
    font-family: "Lato", sans-serif;
  }
  .card-bg-red { fill: var(--cherry); }
  .panel-grey { fill: var(--panel-grey); stroke: var(--bevel); stroke-width: 2; }
  .panel-light { fill: var(--panel-light); stroke: var(--bevel); stroke-width: 2; }
  .panel-white { fill: var(--card-white); stroke: var(--bevel); stroke-width: 2; }
  .company-name { fill: var(--ink-grey); font-size: 34px; font-weight: 400; }
  .company-name-back { font-size: 28px; }
  .tagline { fill: var(--ink-grey); font-size: 22px; }
  .web { fill: #ffffff; font-size: 15px; }
  .person-name { fill: var(--cherry); font-size: 20px; letter-spacing: 0.5px; }
  .person-role { fill: var(--ink-grey); font-size: 15px; }
  .contact-line { fill: var(--ink-grey); font-size: 14px; }
  .label-box { fill: var(--cherry); }
  .label-letter { fill: #ffffff; font-size: 12px; font-weight: 700; }
</style>
</head>
<body>
<main class="canvas">

  <svg class="card card-front" viewBox="0 0 640 366" aria-label="Business card front">
    <rect class="card-bg-red" width="640" height="366"/>
    <polygon class="panel-grey" points="190,-2 642,-2 642,110 460,230 190,120"/>
    <text class="company-name" x="612" y="62" text-anchor="end">Trovan Hire Pty Ltd</text>
    <text class="tagline" x="612" y="92" text-anchor="end">company tagline</text>
    <text class="web" x="30" y="338">www.trovanhire.com.au</text>
  </svg>

  <svg class="card card-back" viewBox="0 0 640 366" aria-label="Business card back">
    <rect class="card-bg-red" width="640" height="366"/>
    <polygon class="panel-light" points="-2,18 312,18 322,40 286,270 -2,262"/>
    <polygon class="panel-white" points="346,40 642,40 642,350 322,350 302,322"/>
    <text class="company-name company-name-back" x="24" y="190">Trovan Hire Pty Ltd</text>

    <g class="contact-block">
      <text class="person-name" x="612" y="82" text-anchor="end">ROS DUNMORE</text>
      <text class="person-role" x="612" y="101" text-anchor="end">director</text>

      <text class="contact-line" x="580" y="140" text-anchor="end">03 9412 5083</text>
      <rect class="label-box" x="590" y="128" width="16" height="16"/>
      <text class="label-letter" x="598" y="141" text-anchor="middle">T</text>

      <text class="contact-line" x="580" y="168" text-anchor="end">0421 736 209</text>
      <rect class="label-box" x="590" y="156" width="16" height="16"/>
      <text class="label-letter" x="598" y="169" text-anchor="middle">M</text>

      <text class="contact-line" x="580" y="196" text-anchor="end">ros.dunmore@trovanhire.com.au</text>
      <rect class="label-box" x="590" y="184" width="16" height="16"/>
      <text class="label-letter" x="598" y="197" text-anchor="middle">E</text>

      <text class="contact-line" x="580" y="224" text-anchor="end">214-220 Pellow Road, Yarraville</text>
      <rect class="label-box" x="590" y="212" width="16" height="16"/>
      <text class="label-letter" x="598" y="225" text-anchor="middle">A</text>
    </g>
  </svg>

</main>
</body>
</html>
```